RK Bastone Construction Inc.

Design a new business card for our construction company
To be removed from current card:
Delete 25 years
Delete Tenant fit up Renovations section

```html
<!DOCTYPE html>
<html lang="en">
<head>
<meta charset="utf-8">
<title>RK Bastone Construction Inc. — Business Card</title>
<link rel="stylesheet" href="https://fonts.googleapis.com/css2?family=Open+Sans:wght@400;700&display=swap">
<style>
  :root {
    --backdrop: #2a2b2d;
    --card: #ffffff;
    --purple: #553278;
    --teal: #217a6d;
    --ink: #2b2b2b;
    --rule: #444444;
  }
  * { box-sizing: border-box; margin: 0; padding: 0; }
  html, body {
    width: 1200px; height: 780px; overflow: hidden;
    background: var(--backdrop);
    font-family: "Open Sans", Arial, sans-serif;
  }
  .canvas { position: relative; width: 1200px; height: 780px; }
  .card {
    position: absolute; top: 236px;
    width: 540px; height: 309px;
    background: var(--card);
    box-shadow: 0 6px 18px rgba(0,0,0,.45);
    overflow: hidden;
  }
  .card--front { left: 40px; }
  .card--back { left: 620px; }

  .wordmark {
    color: var(--purple);
    font-weight: 700;
    text-transform: uppercase;
    letter-spacing: .02em;
    white-space: nowrap;
  }
  .card--front .wordmark {
    position: absolute; left: 0; right: 0; top: 136px;
    text-align: center; font-size: 25px;
  }
  .card--back .wordmark {
    position: absolute; left: 0; right: 0; top: 44px;
    text-align: center; font-size: 19px;
  }

  .holder {
    position: absolute; left: 40px; top: 178px;
    font-size: 24px; font-weight: 700; text-transform: uppercase;
    letter-spacing: .01em; white-space: nowrap;
  }
  .holder__first { color: var(--purple); }
  .holder__last { color: var(--teal); }

  .divider {
    position: absolute; left: 292px; top: 118px;
    width: 1px; height: 108px; background: var(--rule);
  }

  .contacts {
    position: absolute; left: 310px; top: 134px;
    list-style: none; font-size: 12.5px; color: var(--ink);
    white-space: nowrap;
  }
  .contacts li { display: flex; align-items: center; gap: 8px; height: 22px; }
  .contacts svg { width: 13px; height: 13px; flex: none; }

  .address-band {
    position: absolute; left: 0; right: 0; top: 246px; height: 30px;
    background: var(--teal);
    color: #ffffff; font-size: 12.5px; white-space: nowrap;
    display: flex; align-items: center; justify-content: flex-end;
    padding-right: 40px;
  }
</style>
</head>
<body>
<main class="canvas">
  <section class="card card--front" aria-label="Card front">
    <p class="wordmark">RK Bastone Construction Inc.</p>
  </section>

  <section class="card card--back" aria-label="Card back">
    <p class="wordmark">RK Bastone Construction Inc.</p>

    <p class="holder"><span class="holder__first">Marco</span> <span class="holder__last">Bastone</span></p>

    <div class="divider"></div>

    <ul class="contacts">
      <li>
        <svg viewBox="0 0 24 24" aria-hidden="true"><path fill="#217a6d" d="M6.6 10.8a15.1 15.1 0 0 0 6.6 6.6l2.2-2.2c.3-.3.7-.4 1-.2 1.1.4 2.3.6 3.6.6.6 0 1 .4 1 1V20c0 .6-.4 1-1 1A17 17 0 0 1 3 4c0-.6.4-1 1-1h3.5c.6 0 1 .4 1 1 0 1.3.2 2.5.6 3.6.1.3 0 .7-.2 1z"/></svg>
        555-014-2270 ext. 318
      </li>
      <li>
        <svg viewBox="0 0 24 24" aria-hidden="true"><rect x="2" y="5" width="20" height="14" rx="1.5" fill="#217a6d"/><path d="M3 6.5l9 6.5 9-6.5" fill="none" stroke="#fff" stroke-width="1.6"/></svg>
        marco@rkbastoneconst.ca
      </li>
      <li>
        <svg viewBox="0 0 24 24" aria-hidden="true"><circle cx="12" cy="12" r="10" fill="#217a6d"/><path d="M2 12h20M12 2c3 3 3 17 0 20M12 2c-3 3-3 17 0 20" fill="none" stroke="#fff" stroke-width="1.3"/></svg>
        www.rkbastoneconstruction.ca
      </li>
    </ul>

    <div class="address-band">1280 Alder Ridge Rd., Unit 7, Brookmere, NS B3K 2R6</div>
  </section>
</main>
</body>
</html>
```